Potential SF Gazette Best Seller Poetry Book Cover Contest

I’m penning my first poetry book. It’s entitled “Lanterns Under Rain”
I’m fairly open to creative freedom but I want the cover to without a doubt catch a persons' eye instantly because first impressions are VERY IMPORTANT in the literary world
I tend to lean towards a luxury look and colors like black, gold, rose gold, silver, glitter etc but again I’m open to interpretation
Looking forward to your submissions
Target Market(s)
those seeking relatable love advice and quotes
modern millenials
Colors
Look and feel

```html
<!DOCTYPE html>
<html lang="en">
<head>
<meta charset="utf-8">
<title>Lanterns Under Rain — Book Cover</title>
<link rel="stylesheet" href="https://fonts.googleapis.com/css2?family=Kaushan+Script&family=Great+Vibes&family=Open+Sans:wght@400;600;700&display=swap">
<style>
  :root {
    --stage: #f1f1f1;
    --back-top: #763a3c;
    --back-bottom: #4b1b1d;
    --back-text: #f4e6e2;
    --link-pink: #e0707a;
    --front-top: #fdf3ee;
    --front-bottom: #f8e2d6;
    --title-coral: #f0645c;
    --title-wine: #a8283f;
    --ink-red: #d8262c;
    --author-grey: #5a4a48;
  }
  * { box-sizing: border-box; margin: 0; padding: 0; }
  html, body { width: 1200px; height: 800px; overflow: hidden; }
  body {
    background: var(--stage);
    font-family: "Open Sans", sans-serif;
    display: flex;
    align-items: center;
    justify-content: center;
    gap: 40px;
  }
  .cover {
    width: 400px;
    height: 600px;
    position: relative;
    box-shadow: 0 10px 30px rgba(0,0,0,0.18);
  }

  /* Back cover */
  .back-cover {
    background: linear-gradient(160deg, var(--back-top), var(--back-bottom));
    color: var(--back-text);
    padding: 38px 48px 30px;
    text-align: center;
    overflow: hidden;
  }
  .back-title {
    font-family: "Kaushan Script", cursive;
    font-weight: 400;
    font-size: 54px;
    line-height: 1.2;
    color: #fff;
    margin-bottom: 22px;
  }
  .blurb {
    font-size: 9.5px;
    line-height: 1.5;
    text-align: left;
    margin-bottom: 12px;
  }
  .author-heading {
    font-weight: 700;
    font-size: 17px;
    letter-spacing: 0.5px;
    margin: 16px 0 12px;
    color: #fff;
  }
  .website-label {
    font-weight: 700;
    font-size: 9px;
    line-height: 1.4;
    margin-top: 22px;
    color: #fff;
  }
  .website-url {
    font-size: 9px;
    letter-spacing: 0.5px;
    color: var(--link-pink);
    margin-top: 12px;
  }

  /* Front cover */
  .front-cover {
    background: linear-gradient(180deg, var(--front-top), var(--front-bottom));
    overflow: hidden;
  }
  .title {
    position: absolute;
    top: 48px;
    left: 0;
    width: 100%;
    text-align: center;
    line-height: 1;
  }
  .title-script {
    display: block;
    font-family: "Great Vibes", cursive;
    font-size: 82px;
    color: var(--title-coral);
    transform: rotate(-4deg);
  }
  .title-bold {
    display: block;
    font-family: "Kaushan Script", cursive;
    font-size: 50px;
    color: var(--title-wine);
    margin-top: -6px;
    transform: rotate(4deg);
  }
  .cover-art {
    position: absolute;
    left: 45px;
    top: 200px;
    width: 310px;
    height: 300px;
    border-radius: 50%;
    background:
      radial-gradient(circle at 60% 62%, #d63a3a 0 24%, #8e1e30 30%, transparent 42%),
      radial-gradient(circle at 38% 40%, #9c9c9c 0 18%, transparent 38%),
      radial-gradient(circle, #f3ddd3 0 55%, rgba(248,226,214,0) 72%);
  }
  .ink-swash {
    position: absolute;
    left: 60px;
    top: 500px;
  }
  .author-name {
    position: absolute;
    top: 550px;
    width: 100%;
    text-align: center;
    font-size: 12px;
    letter-spacing: 0.4px;
    color: var(--author-grey);
  }
</style>
</head>
<body>
  <section class="cover back-cover">
    <h2 class="back-title">Back Cover</h2>
    <p class="blurb">Lorem ipsum dolor sit amet, consectetuer adipiscing elit. Vivamus varius facilisis eros. Sed erat. In in velit quis arcu ornare luctus. Integer ut purus ac augue commodo commodo. Nunc nec mi eu justo tempor consectetuer. Etiam vitae nisl. Cras elit lectus, bibendum a, adipiscing vitae. Ut tincidunt tortor.</p>
    <p class="blurb">Donec nonummy, enim in lacinia pulvinar, velit tellus posuere libero, urna eget neque. Cras ipsum. Vestibulum venenatis volutpat, purus lectus ultrices risus. Nullam quam. Pellentesque auctor fringilla neque. Duis vestibulum. Maecenas facilisis elit sed justo. Quisque.</p>
    <p class="blurb">Fusce auctor, metus eu ultricies vulputate, sapien nibh sollicitudin augue risus et dolor. Aenean pellentesque ullamcorper ligula, ac vestibulum neque. Nam nisi. Praesent laoreet ante tempor urna. In fermentum nonummy. Cras vel nunc. Donec rhoncus. Phasellus tempus massa et quet.</p>
    <h3 class="author-heading">AUTHER NAME</h3>
    <p class="blurb">Lorem ipsum dolor sit amet, consectetuer facilisis eros. Sed erat. In in velit quis arcu ornare luctus massa. Integer ut purus ac augue commodo justo tempor consectetuer.</p>
    <p class="website-label">VISIT THE AUTHORS<br>WEBSITE AT:</p>
    <p class="website-url">WWW.QUILLANDPAGE.COM</p>
  </section>

  <section class="cover front-cover">
    <h1 class="title">
      <span class="title-script">Lanterns</span>
      <span class="title-bold">Under Rain</span>
    </h1>
    <div class="cover-art" role="img" aria-label="Illustration of a grey quill feather beside a red glass heart-shaped ink bottle, with red ink splatters and a pale sunburst behind"></div>
    <svg class="ink-swash" width="280" height="40" viewBox="0 0 280 40" aria-hidden="true">
      <path d="M0 12 C60 4 110 8 150 20 C190 30 240 28 280 36 C230 34 190 36 150 28 C110 20 60 16 0 12 Z" fill="var(--ink-red)"/>
    </svg>
    <p class="author-name">AOUTHER NAME</p>
  </section>
</body>
</html>
```